Create a Website Layout for a Tourism Company

We need a clean and easy to navigate layout for a turism company, the layout must be a mix between Nature and City. The page must contain at least one link to a page with topics that can be sorted by type or alphabetic. Those topics must be something like this website " http://www.lunavento.com.br/compra-coletiva/rio-de-janeiro/ "

Good Luck

```html
<!DOCTYPE html>
<html lang="en">
<head>
<meta charset="utf-8">
<title>Maré Alta Guides</title>
<link rel="stylesheet" href="https://fonts.googleapis.com/css2?family=Arimo:wght@400;700&family=PT+Sans:ital,wght@0,400;0,700;1,400&display=swap">
<style>
:root{
  --header-bg:#f6f9fb;
  --green:#8cbf1f;
  --green-dark:#6a9a1f;
  --link-blue:#1f5f9e;
  --red:#c0141b;
  --teal-dark:#15857a;
  --orange:#f57f20;
  --lime:#d4ef6e;
  --nav-bg:#2cc9bb;
  --footer-bg:#52d8cf;
  --post-bg:#eef8f8;
  --rule-red:#e88a86;
  --text-grey:#555;
  --title-grey:#4a4a4a;
  --btn-red:#d0240f;
}
*{box-sizing:border-box;margin:0;padding:0}
html,body{width:1041px;height:1200px;overflow:hidden;background:#fff;font-family:Arimo,Arial,sans-serif;color:var(--text-grey)}
.page{position:relative;width:1041px;height:1200px}
.abs{position:absolute}
.header-band{left:0;top:0;width:1041px;height:185px;background:var(--header-bg)}
.brand{left:217px;top:40px;display:flex;align-items:center;gap:10px;font-family:"PT Sans",sans-serif;font-weight:700;font-size:30px;color:var(--green)}
.brand-mark{width:22px;height:22px;background:var(--green)}
.lang-box{left:729px;top:14px;width:99px;height:25px;background:#fff;border:1px solid #e3e6e8;border-radius:3px;display:flex;align-items:center;gap:10px;padding-left:10px}
.flag{width:22px;height:14px}
.account-links{left:676px;top:46px;font-size:10px;color:var(--link-blue)}
.account-links span{margin:0 5px;color:#888}
.search{left:676px;top:65px;width:152px;height:24px;display:flex;border:1px solid #d9dde0;background:#fff;font-size:9px;color:var(--link-blue)}
.search .scope{padding:6px 0 0 4px;width:28px}
.search .field{padding-top:6px;flex:1}
.search .go{width:32px;background:var(--green-dark);color:#fff;font-weight:700;text-align:center;padding-top:6px}
.welcome{left:463px;top:82px;font-family:"PT Sans",sans-serif;font-style:italic;color:var(--green);white-space:nowrap}
.welcome .big{font-size:60px}
.welcome .small{font-size:34px}
.nav{left:201px;top:147px;width:639px;height:35px;background:var(--nav-bg);border-radius:4px 4px 0 0;display:flex;gap:3px;padding:0 12px;align-items:flex-end}
.nav a{height:32px;flex:1;color:#fff;font-weight:700;font-size:12px;text-decoration:none;display:flex;align-items:center;justify-content:center}
.nav .home{background:var(--red)}
.nav .hotels{background:var(--teal-dark)}
.nav .flights{background:var(--green-dark)}
.nav .rentals{background:var(--orange)}
.nav .best{background:var(--lime);color:var(--red)}
.hero{left:201px;top:187px;width:639px;height:167px;background:linear-gradient(180deg,#6c97c6 0%,#3d6a8c 45%,#2c5a6e 70%,#4d6a3c 100%)}
.hero-caption{left:201px;top:272px;width:325px;height:46px;background:rgba(30,60,90,.45);color:#fff;font-family:"PT Sans",sans-serif;font-style:italic;font-size:38px;padding-left:20px;line-height:46px}
.post{left:201px;width:639px;height:162px;background:linear-gradient(90deg,#f3fafa,var(--post-bg))}
.post-photo{position:absolute;left:12px;top:7px;width:286px;height:153px}
.post-body{position:absolute;left:309px;top:8px;width:318px}
.post-title{font-size:14px;color:var(--title-grey);line-height:15px;padding-bottom:8px;border-bottom:1px solid var(--rule-red)}
.post-text{font-size:9.6px;line-height:11.5px;margin-top:6px}
.post-foot{position:absolute;left:309px;top:133px;width:318px;height:22px}
.post-foot .line{position:absolute;left:0;right:108px;top:11px;border-top:1px solid var(--rule-red)}
.read-more{position:absolute;right:22px;top:0;width:81px;height:22px;background:var(--btn-red);border-radius:3px;color:#fff;font-size:10.5px;font-weight:700;text-align:center;line-height:22px;word-spacing:9px}
.pager-strip{left:201px;top:873px;width:639px;height:35px;background:#eef8f8;font-size:10px;color:#666}
.pager-strip .pages{position:absolute;right:40px;top:14px;letter-spacing:2px}
.pager-strip b{color:var(--red)}
.footer{left:201px;top:908px;width:639px;height:266px;background:var(--footer-bg);border-radius:0 0 4px 4px;color:#fff}
.col{position:absolute;top:12px;width:142px}
.col h3{font-weight:400;font-size:12px;color:#153f40;padding-bottom:6px;border-bottom:1px solid #fff}
.col h4{font-weight:400;font-size:12px;color:#153f40;margin:12px 0 4px}
.col p{font-size:7.8px;line-height:10px}
.thumb{width:142px;height:78px;margin-top:10px;background:linear-gradient(180deg,#8eb0cf,#5d7a52)}
.mini-btn{display:block;width:44px;height:12px;background:var(--btn-red);border-radius:2px;font-size:6px;text-align:center;line-height:12px;color:#fff}
.quote{font-size:7.8px;line-height:10px;padding:8px 0 6px;border-bottom:1px solid #fff}
.archive li{list-style:none;font-size:7.8px;padding:4px 0 2px;border-bottom:1px solid #fff}
.archive li.gap{border:none;padding-bottom:10px}
.social{display:flex;gap:3px;margin-top:4px}
.social i{width:15px;height:15px;border-radius:3px;background:#2c6da8}
.copyright{left:12px;top:246px;font-size:9.5px;color:#153f40}
</style>
</head>
<body>
<div class="page">
  <div class="abs header-band"></div>
  <div class="abs brand"><span class="brand-mark"></span>Maré Alta Guides</div>
  <div class="abs lang-box">
    <svg class="flag" viewBox="0 0 22 14"><rect width="22" height="14" fill="#1c9a3c"/><path d="M11 2 20 7 11 12 2 7Z" fill="#f5d100"/><circle cx="11" cy="7" r="3" fill="#1f3f8f"/></svg>
    <svg class="flag" viewBox="0 0 22 14"><rect width="22" height="14" fill="#1f3f8f"/><path d="M0 0 22 14M22 0 0 14" stroke="#fff" stroke-width="3"/><path d="M11 0V14M0 7H22" stroke="#fff" stroke-width="4"/><path d="M11 0V14M0 7H22" stroke="#c8102e" stroke-width="2"/></svg>
    <svg width="12" height="9" viewBox="0 0 12 9"><path d="M0 0H12L6 9Z" fill="var(--green)"/></svg>
  </div>
  <div class="abs account-links">My Account<span>|</span>Log In<span>|</span>Checkout</div>
  <div class="abs search"><span class="scope">All ▾</span><span class="field">Quick search</span><span class="go">GO ›</span></div>
  <div class="abs welcome"><span class="big">Welcome</span> <span class="small">to Maré Alta</span></div>

  <nav class="abs nav">
    <a class="home" href="#">HOME</a>
    <a class="hotels" href="#">HOTELS</a>
    <a class="flights" href="#">FLIGHTS</a>
    <a class="rentals" href="#">VACATION RENTALS</a>
    <a class="best" href="#">BEST OF 2013</a>
  </nav>

  <div class="abs hero" role="img" aria-label="Panorama of a mountain peak over a blue bay and the city shore"></div>
  <div class="abs hero-caption">Welcome to RIO</div>

  <article class="abs post" style="top:362px">
    <div class="post-photo" role="img" aria-label="City bay seen from a hilltop statue lookout" style="background:linear-gradient(180deg,#7fa6d4,#2f6ea0 50%,#4f7a4a)"></div>
    <div class="post-body">
      <div class="post-title">Lorem ipsum dolor, August 15 to 27, 2013<br>(Quest &amp; One Tips)</div>
      <p class="post-text">Lorem ipsum dolor sit amet, consectetur adipiscing elit. Sed blandit massa vel mauris sollicitudin dignissim. Phasellus ultrices tellus eget ipsum ornare molestie scelerisque eros dignissim. Phasellus fringilla hendrerit lectus nec vehicula.</p>
      <p class="post-text" style="margin-top:12px">Pellentesque habitant morbi tristique senectus et netus et malesuada fames ac turpis egestas. In faucibus, risuntesque,...</p>
    </div>
    <div class="post-foot"><span class="line"></span><span class="read-more">Read more</span></div>
  </article>

  <article class="abs post" style="top:531px">
    <div class="post-photo" role="img" aria-label="River winding through green forest" style="background:linear-gradient(180deg,#a9c8e6,#3e7a3a 45%,#6b5a40 75%,#2f5a2e)"></div>
    <div class="post-body">
      <div class="post-title">Lorem ipsum dolor, August 15 to 27, 2013<br>(Quest &amp; One Tips)</div>
      <p class="post-text">Lorem ipsum dolor sit amet, consectetur adipiscing elit. Sed blandit massa vel mauris sollicitudin dignissim. Phasellus ultrices tellus eget ipsum ornare molestie scelerisque eros dignissim. Phasellus fringilla hendrerit lectus nec vehicula.</p>
      <p class="post-text" style="margin-top:12px">Pellentesque habitant morbi tristique senectus et netus et malesuada fames ac turpis egestas. In faucibus, risuntesque,...</p>
    </div>
    <div class="post-foot"><span class="line"></span><span class="read-more">Read more</span></div>
  </article>

  <article class="abs post" style="top:700px">
    <div class="post-photo" role="img" aria-label="Curved city beach with mountains behind" style="background:linear-gradient(180deg,#9ab8d8,#6f7f86 40%,#d8c8a8 60%,#3e6a3a)"></div>
    <div class="post-body">
      <div class="post-title">Lorem ipsum dolor, August 15 to 27, 2013<br>(Quest &amp; One Tips)</div>
      <p class="post-text">Lorem ipsum dolor sit amet, consectetur adipiscing elit. Sed blandit massa vel mauris sollicitudin dignissim. Phasellus ultrices tellus eget ipsum ornare molestie scelerisque eros dignissim. Phasellus fringilla hendrerit lectus nec vehicula.</p>
      <p class="post-text" style="margin-top:12px">Pellentesque habitant morbi tristique senectus et netus et malesuada fames ac turpis egestas. In faucibus, risuntesque,...</p>
    </div>
    <div class="post-foot"><span class="line"></span><span class="read-more">Read more</span></div>
  </article>

  <div class="abs pager-strip"><span class="pages"><b>1</b> 2 3 4 5 6 <b>&gt;&gt;</b></span></div>

  <footer class="abs footer">
    <div class="col" style="left:12px">
      <h3>Our Work</h3>
      <div class="thumb" role="img" aria-label="Cable car above a green hillside"></div>
      <p style="margin:12px 0 18px">Lorem ipsum dolor sit amet, consectetur adipiscing elit. Sed blandit massa vel mauris sollicitudin dignissim. Phasellus ultrices tellus eget ipsum ornare molestie scelerisque eros dignissim.........</p>
      <span class="mini-btn">Read more</span>
    </div>
    <div class="col" style="left:168px">
      <h3>About Us</h3>
      <h4>Lorem Ipsum</h4>
      <p style="padding-bottom:8px;border-bottom:1px solid #fff">Lorem ipsum dolor sit amet, consectetur adipiscing elit. Sed blandit massa vel mauris sollicitudin dignissim. Phasellus ultrices tellus eget ipsum ornare molestie scelerisque eros dignissim.........</p>
      <h4>Lorem Ipsum</h4>
      <p style="margin-bottom:18px">Lorem ipsum dolor sit amet, consectetur adipiscing elit. Sed blandit massa vel mauris sollicitudin dignissim. Phasellus ultrices tellus eget ipsum ornare molestie scelerisque eros dignissim.........</p>
      <span class="mini-btn">Read more</span>
    </div>
    <div class="col" style="left:324px">
      <h3>Travel Quotes</h3>
      <div class="quote">Lorem ipsum dolor sit amet, consectetur adipiscing elit.</div>
      <div class="quote">Lorem ipsum dolor sit amet, consectetur adipiscing elit.</div>
      <div class="quote">Lorem ipsum dolor sit amet, consectetur adipiscing elit.</div>
      <div class="quote">Lorem ipsum dolor sit amet, consectetur adipiscing elit.</div>
      <div class="quote">Lorem ipsum dolor sit amet, consectetur adipiscing elit.</div>
      <p style="margin-top:28px;font-size:7px">Follow us on</p>
      <div class="social"><i></i><i></i><i></i><i></i><i></i></div>
    </div>
    <div class="col" style="left:480px">
      <h3>Archives</h3>
      <ul class="archive" style="margin-top:8px">
        <li>JANUARY 2013</li><li>FEBRUARY 2013</li><li>MARCH 2013</li><li>APRIL 2013</li><li>MAY 2013</li><li class="gap">JUNE 2013</li>
        <li>2012</li><li>2011</li><li>2010</li>
      </ul>
    </div>
    <div class="abs copyright">Copyright &nbsp;2013 | &nbsp;Site by</div>
  </footer>
</div>
</body>
</html>
```